Box for a Bold Bathroom - stylish minimalist package for a modern upscale brand

We need an adaptable package design using a color label on a brown box, or just a brown box with 2 or 3 color printing. The best design would be one that is adaptable for either use.

Our first products launching under this brand will be a series of medicine cabinets and mirrors, and our cartons can vary in size from 500x100x600 mm to 1200x300x1000 mm

About us: we produce a variety of bathroom fixtures including medicine cabinets, mirrors, vanities, etc. You've likely seen our products - we do manufacturing for Valdrane, Murtello, Fenwick Hollow, Dunmore & Pike, and others.

A version of our logo is attached for reference; we use it in a variety of color mixes depending on application. Vector available if needed or can be used FPO and our team will replace.

These are our colors, please take note and ignore the 'color' field:

Light Blue: C:66%/M:6%/Y:22%/K:0%; H:189° S:65% B:78%
Light Grey: C:35%/M:26%/Y:24%/K:0%; H:213° S:5% B:70%
Dark Blue: C:90%/M:50%/Y:44%/K:20%; H:189° S:82% B:43%
Dark Grey: C:70%/M:60%/Y:54%/K:38%; H:213° S:11% B:30%

Project Deadline Extended
Reason: Some revisions still outstanding before we can make selection, and some submissions we have agreed to wait for. Please submit all work ASAP so our team can provide feedback to you. Thanks!

Target Market(s)

DIY'ers; home renovators

Industry/Entity Type

Home Improvement

Font styles to use
Sans Serif

Requirements
Must have
• 1. Brand logo w/ logotype
• 2. Brand name without logo (can be on shipping mark side)
• 3. Multi-lingual En/Fr/Es (you do not need to include multi-lingual content but must allow space for our own translations if you do not)
• 4. Shipping/Handling Glyphs on 5 sides (all but bottom)
• i.e. fragile, this way up, team lift or mech lift, clamp or no clamp, max-stack
• 5. Two sides should include a marked 4" x 4" area for affixing labels (e.g. UPC, SSCC, etc.) ideally with a dotted line or corner marks or similar.
• 6. Shipping mark details or space for them (should be on the smallest side, only needed on one but can be on both) [see example file of shipping mark informations]
Nice to have
• Design that can be used either with color label on brown box, or brown box only.
• If designing for color label; please see the sample images included. Lifestyle should be prominent, the inside photo being smaller to help show interior features. These photos are obviously not useful for brown-box design.

```html
<!DOCTYPE html>
<html lang="en">
<head>
<meta charset="utf-8">
<title>Tidewell Carton Packaging</title>
<link rel="stylesheet" href="https://fonts.googleapis.com/css2?family=Jost:wght@400;500&display=swap">
<style>
  :root {
    --light-blue: #46b7c7;
    --light-grey: #aaaeb3;
    --dark-blue: #14636e;
    --dark-grey: #444a4f;
    --label-grey: #c4c7cb;
    --label-white: #dde0e4;
    --kraft: #d8a679;
    --kraft-edge: #c99463;
    --backdrop: #e6e8ea;
    --ink: #3a3e42;
  }
  * { box-sizing: border-box; margin: 0; padding: 0; }
  html, body { width: 1068px; height: 1200px; overflow: hidden; }
  body {
    background: var(--backdrop);
    font-family: "Jost", sans-serif;
    position: relative;
  }
  .kraft {
    position: absolute;
    background: var(--kraft);
    border: 1px solid var(--kraft-edge);
  }
  .label {
    position: absolute;
    overflow: hidden;
  }
  .circle {
    position: absolute;
    border-radius: 50%;
  }
  .brand {
    position: absolute;
    font-weight: 500;
    letter-spacing: 0.12em;
    text-transform: uppercase;
    white-space: nowrap;
  }
  .glyphs { position: absolute; }

  /* Top: carton face with label panels */
  .carton-top { left: 40px; top: 40px; width: 988px; height: 520px; }

  .front-label { left: 80px; top: 80px; width: 380px; height: 440px; background: var(--label-grey); }
  .front-label .brand { right: 24px; top: 22px; font-size: 18px; color: var(--ink); }
  .front-label .circle-top { width: 220px; height: 220px; left: 80px; top: 66px; background: var(--dark-blue); }
  .front-label .circle-bottom { width: 300px; height: 300px; left: 40px; top: 320px; background: #1f8694; }
  .front-label .glyphs { left: 160px; top: 350px; }

  .info-label { left: 500px; top: 80px; width: 488px; height: 440px; background: var(--label-white); }
  .info-label .brand { right: 28px; top: 22px; font-size: 22px; color: var(--ink); }
  .info-label .circle-side { width: 240px; height: 240px; left: -150px; top: 260px; background: #1f8694; }
  .info-copy {
    position: absolute; left: 110px; top: 66px; width: 250px;
    font-size: 8.5px; line-height: 1.35; color: var(--ink);
  }
  .info-copy p + p { margin-top: 6px; }
  .label-area { position: absolute; left: 150px; top: 240px; width: 150px; height: 150px; }
  .info-label .glyphs { right: 28px; bottom: 24px; }

  /* Bottom: kraft boards with colour labels */
  .board-large { left: 300px; top: 600px; width: 560px; height: 460px; }
  .board-small { left: 200px; top: 780px; width: 300px; height: 380px; }

  .dark-label { left: 560px; top: 700px; width: 300px; height: 360px; background: var(--dark-grey); }
  .dark-label .brand { left: 0; right: 0; text-align: center; top: 26px; font-size: 18px; color: #c9ccd0; }
  .dark-label .circle-main { width: 160px; height: 160px; left: 66px; top: 100px; background: var(--light-blue); }
  .dark-label .circle-corner { width: 130px; height: 130px; left: 190px; top: 255px; background: #37a9b7; }

  .light-label { left: 370px; top: 960px; width: 130px; height: 200px; background: var(--light-grey); }
  .light-label .brand { left: 0; right: 0; text-align: center; top: 14px; font-size: 10px; color: var(--ink); }
  .light-label .circle-main { width: 84px; height: 84px; left: 35px; top: 54px; background: var(--dark-blue); }
  .light-label .circle-corner { width: 66px; height: 66px; left: 96px; top: 146px; background: var(--dark-blue); }
</style>
</head>
<body>

  <!-- Carton face -->
  <div class="kraft carton-top"></div>

  <section class="label front-label">
    <div class="brand">Tidewell</div>
    <div class="circle circle-top"></div>
    <div class="circle circle-bottom"></div>
    <svg class="glyphs" width="70" height="34" viewBox="0 0 70 34" aria-label="Fragile, this way up">
      <g fill="#1d3c43">
        <path d="M2 2h18v8a9 9 0 0 1-7 8.8V27h6v3H3v-3h6v-8.2A9 9 0 0 1 2 10z"/>
        <path d="M34 30h32v3H34z"/>
        <path d="M41 26V12h-5l7-9 7 9h-5v14z"/>
        <path d="M55 26V12h-5l7-9 7 9h-5v14z"/>
      </g>
    </svg>
  </section>

  <section class="label info-label">
    <div class="circle circle-side"></div>
    <div class="brand">Tidewell</div>
    <div class="info-copy">
      <p>Two storage zones in one cabinet: shelves behind the mirror hold bottles and small jars. Soft rounded corners make it suited to tight spaces, and the safety film on the back lowers the risk of injury if glass breaks.</p>
      <p>Two storage zones in one cabinet: shelves behind the mirror hold bottles and small jars. Soft rounded corners make it suited to tight spaces, and the safety film on the back lowers the risk of injury if glass breaks.</p>
      <p>Two storage zones in one cabinet: shelves behind the mirror hold bottles and small jars. Soft rounded corners make it suited to tight spaces, and the safety film on the back lowers the risk of injury if glass breaks.</p>
    </div>
    <svg class="label-area" viewBox="0 0 150 150" aria-label="4 by 4 inch label area">
      <g fill="none" stroke="#8e9297" stroke-width="2">
        <path d="M2 22V2h20"/>
        <path d="M128 2h20v20"/>
        <path d="M148 128v20h-20"/>
        <path d="M22 148H2v-20"/>
      </g>
    </svg>
    <svg class="glyphs" width="70" height="34" viewBox="0 0 70 34" aria-label="Fragile, this way up">
      <g fill="#4a4f54">
        <path d="M2 2h18v8a9 9 0 0 1-7 8.8V27h6v3H3v-3h6v-8.2A9 9 0 0 1 2 10z"/>
        <path d="M34 30h32v3H34z"/>
        <path d="M41 26V12h-5l7-9 7 9h-5v14z"/>
        <path d="M55 26V12h-5l7-9 7 9h-5v14z"/>
      </g>
    </svg>
  </section>

  <!-- Kraft boards with colour labels -->
  <div class="kraft board-large"></div>
  <div class="kraft board-small"></div>

  <section class="label dark-label">
    <div class="brand">Tidewell</div>
    <div class="circle circle-main"></div>
    <div class="circle circle-corner"></div>
  </section>

  <section class="label light-label">
    <div class="brand">Tidewell</div>
    <div class="circle circle-main"></div>
    <div class="circle circle-corner"></div>
  </section>

</body>
</html>
```